Marlow Aviation Group Envelope, Letterhead, Business Card Design

I need designs for a new company letterhead, business cards, and envelopes. These designs will need to be presented using 5 different company logos for the different divisions that are managed under the Marlow Aviation Group umbrella (company names listed below). The member of FRCU logo should also be included.
- Marlow Aviation Group
- Marlow Jet Management
- Marlow Jet Charter
- Marlow Pilot Services
- Marlow Aircraft Sales
- Marlow Flight Training

Logos for the various companies are attached as well as a screen shot of the main page of our website.

```html
<!DOCTYPE html>
<html lang="en">
<head>
<meta charset="utf-8">
<title>Marlow Aviation Group – Envelope</title>
<link rel="stylesheet" href="https://fonts.googleapis.com/css2?family=Montserrat:wght@400;500;600&display=swap">
<style>
  :root {
    --backdrop: #4b5157;
    --paper-light: #f7f8f8;
    --paper-shade: #e9ebeb;
    --watermark: rgba(255, 255, 255, 0.6);
    --brand-blue: #1f64b8;
    --ink: #1d1f21;
    --ink-soft: #55595d;
  }
  * { box-sizing: border-box; margin: 0; padding: 0; }
  html, body {
    width: 1200px;
    height: 900px;
    overflow: hidden;
    background: var(--backdrop);
    font-family: "Montserrat", sans-serif;
  }
  .envelope {
    position: absolute;
    left: 80px;
    top: 205px;
    width: 1040px;
    height: 490px;
    overflow: hidden;
    background: linear-gradient(115deg, var(--paper-shade) 0%, var(--paper-light) 70%);
    box-shadow: 0 10px 30px rgba(0,0,0,0.25);
  }
  .watermark {
    position: absolute;
    left: 0;
    top: 0;
    width: 1040px;
    height: 490px;
  }
  .brand-name {
    position: absolute;
    left: 60px;
    top: 70px;
    display: flex;
    align-items: center;
    gap: 14px;
    font-size: 30px;
    font-weight: 600;
    letter-spacing: 0.06em;
    text-transform: uppercase;
    color: var(--brand-blue);
  }
  .brand-dot {
    width: 18px;
    height: 18px;
    border-radius: 50%;
    background: var(--brand-blue);
  }
  .return-address {
    position: absolute;
    left: 60px;
    bottom: 60px;
    font-size: 13px;
    font-style: normal;
    font-weight: 500;
    line-height: 1.4;
    letter-spacing: 0.04em;
    text-transform: uppercase;
    color: var(--ink);
  }
  .return-address .web {
    color: var(--brand-blue);
  }
  .membership {
    position: absolute;
    right: 60px;
    top: 200px;
  }
  .membership-label {
    display: block;
    font-size: 9px;
    color: var(--ink-soft);
    margin-left: 40px;
    margin-bottom: 2px;
  }
  .membership-mark {
    display: flex;
    align-items: center;
    gap: 8px;
    font-size: 22px;
    font-weight: 500;
    letter-spacing: 0.05em;
    color: var(--ink-soft);
  }
  .membership-badge {
    width: 30px;
    height: 30px;
    border-radius: 50%;
    background: var(--brand-blue);
  }
</style>
</head>
<body>
  <div class="envelope">
    <svg class="watermark" viewBox="0 0 1040 490" role="img" aria-label="Large faint brand decoration across the envelope face">
      <circle cx="560" cy="330" r="300" fill="var(--watermark)"/>
    </svg>

    <div class="brand-name">
      <span class="brand-dot"></span>
      <span>Marlow Aviation Group</span>
    </div>

    <div class="membership">
      <span class="membership-label">member of</span>
      <div class="membership-mark">
        <span class="membership-badge"></span>
        <span>FRCU</span>
      </div>
    </div>

    <address class="return-address">
      48 Harbor Lane<br>
      Eastbrook, New York<br>
      12790<br>
      <span class="web">www.marlowaviation.com</span>
    </address>
  </div>
</body>
</html>
```